Water Filtration Company needs a business card design using our existing logo/colours!

We design and manufacture and export specialised water filtration equipment. Our equipment will take unclean dirty water and filters to safe clean drinkable water.
We would like to see designs using our existing logo and colours (see attached "Palette") that represents clean safe drinking water (fresh, clean designs but still professional and modern). Our customers are other businesses who supply water filtration equipment, governments, and private individuals.
BUSINESS CARD DETAILS (Common details):
Tel: + 61 7 55 419 276
www: brindlepeak.com.au
Address: 3/47 Cordwell Parade
Marlow Flats NSW 2593 Australia
(please include the word Australia as we are an international company)
Must include: COMMERCIAL WATER FILTRATION EQUIPMENT
NAME NO 1:
Owen Pritch
General Manager
Mobile: +61 427 38 91 04
Email: owen@brindlepeak.com.au
NAME NO. 2:
Gina Rosk
Business Manager
Mobile: +61 409 572 148
Email: gina@brindlepeak.com.au
Must Have:
1) PRINT READY IN .AI & .PDF FORMATS
2) Also saved in file format .ai (Adobe Illustrator - compatible with CS4)
3) Use existing LOGO & COLOURS: Please use our logo (see attached file)
4) FONTS: we have used Avenir & Helvetica in the past but are open to other font types for the address etc.
Thank you!

```html
<!DOCTYPE html>
<html lang="en">
<head>
<meta charset="utf-8">
<title>Brindle Peak – Business Cards</title>
<link rel="stylesheet" href="https://fonts.googleapis.com/css2?family=Source+Sans+3:wght@400;600&family=Arimo:wght@400;700&display=swap">
<style>
  :root {
    --page-bg: #ffffff;
    --frame: #b9e2ea;
    --frame-line: #bfe3ea;
    --brand-blue: #0a5f86;
    --text-grey: #555a5e;
    --name-grey: #55595c;
    --tint-left: #cfe9ef;
    --tint-mid: #b5d7e0;
    --tint-right: #c8dde5;
    --ornament: #eef8fa;
  }
  * { box-sizing: border-box; margin: 0; padding: 0; }
  html, body { width: 1200px; height: 1000px; overflow: hidden; background: var(--page-bg); }
  body { position: relative; font-family: "Source Sans 3", "Myriad Pro", sans-serif; }

  .card { position: absolute; border: 7px solid var(--frame); background: #fff; }
  .card-front { left: 278px; top: 101px; width: 644px; height: 364px; }
  .card-back  { left: 279px; top: 508px; width: 645px; height: 365px; }

  .inner-rule { position: absolute; left: 5px; top: 5px; right: 5px; bottom: 5px; border: 2px solid var(--frame-line); }

  .brand-name {
    position: absolute; left: 0; right: 0; top: 40px;
    text-align: center; font-weight: 600;
    font-size: 92px; line-height: 1; letter-spacing: 1px; color: var(--brand-blue);
  }
  .brand-ornament { position: absolute; left: 526px; top: 150px; width: 92px; height: 182px; }

  .contact-block {
    position: absolute; left: 0; right: 0; top: 200px;
    text-align: center; font-size: 19.5px; line-height: 24.5px; color: var(--text-grey);
  }

  .back-art {
    position: absolute; left: 6px; top: 6px; width: 620px; height: 339px;
    background: linear-gradient(90deg, var(--tint-left) 0%, var(--tint-right) 45%, var(--tint-mid) 70%, var(--tint-right) 100%);
  }

  .person { position: absolute; left: 57px; top: 108px; color: var(--text-grey); }
  .person-name { font-family: "Arimo", Helvetica, sans-serif; font-weight: 700; font-size: 22px; color: var(--name-grey); line-height: 26px; }
  .person-title { font-size: 19px; line-height: 22px; }
  .person-contact { margin-top: 36px; font-size: 20.5px; line-height: 30px; }
</style>
</head>
<body>

<section class="card card-front">
  <div class="inner-rule"></div>
  <div class="brand-name">Brindle Peak</div>
  <svg class="brand-ornament" viewBox="0 0 92 182" role="img" aria-label="Faint leaf and water-drop ornament">
    <rect width="92" height="182" rx="36" fill="var(--ornament)"/>
  </svg>
  <div class="contact-block">
    <p>Tel: + 61 7 55 419 276</p>
    <p>www: brindlepeak.com.au</p>
    <p>Address: 3/47 Cordwell Parade</p>
    <p>Marlow Flats NSW 2593 Australia</p>
    <p>COMMERCIAL WATER FILTRATION EQUIPMENT</p>
  </div>
</section>

<section class="card card-back">
  <div class="inner-rule" style="border-color:#ffffff;border-width:5px;left:1px;top:1px;right:1px;bottom:1px;"></div>
  <div class="back-art" role="img" aria-label="Soft blue leaf and water swoosh illustration"></div>
  <div class="person">
    <p class="person-name">Owen Pritch</p>
    <p class="person-title">General Manager</p>
    <div class="person-contact">
      <p>Mobile: +61 427 38 91 04</p>
      <p>Email: owen@brindlepeak.com.au</p>
    </div>
  </div>
</section>

</body>
</html>
```